New Wix logo and website layout

I need a new logo design and a new, modern website layout design. I am a professional therapist providing remedial massage. I am Canadian but live in Australia & would like the logo to have a somewhat 'Canadian feel' to it (something subtle i.e. no flags) I currently have a maple tree leaf as my logo. my current website is stonebaymassage.com.au. I need the website to work on mobile phones & traditional web browsers.

Target Market(s)

customers looking for remedial massage and manual lymphatic drainage

Industry/Entity Type

professional massage

Coding

Coded - Design and coding required

Font styles to use
Sans Serif

Colors
EB3D1F
EC4F4E
F09395
F8D3D4
FCEDEE

Requirements
Nice to have
• something subtle that indicates that I am canadian
Should not have
• no flags. nothing too bold

```html
<!DOCTYPE html>
<html lang="en">
<head>
<meta charset="utf-8">
<title>Stone Bay Massage</title>
<link rel="stylesheet" href="https://fonts.googleapis.com/css2?family=Libre+Baskerville:wght@400;700&family=Lato:wght@400;700&family=Rubik:wght@400;500;700&display=swap">
<style>
:root{
  --red:#EB3D1F;
  --rose:#EC4F4E;
  --salmon:#F09395;
  --blush:#F8D3D4;
  --mist:#FCEDEE;
  --ink:#333;
  --white:#fff;
}
*{box-sizing:border-box;margin:0;padding:0}
html,body{width:1200px;height:3567px;overflow:hidden}
body{position:relative;background:var(--white);font-family:'Lato',sans-serif;color:var(--ink)}
.abs{position:absolute}
.serif{font-family:'Libre Baskerville',serif}
.section-title{position:absolute;left:0;width:1200px;text-align:center;font-family:'Libre Baskerville',serif;font-weight:700;color:var(--red);font-size:35px;letter-spacing:.5px}

/* header */
.site-header{position:absolute;left:0;top:0;width:1200px;height:115px;background:var(--white);box-shadow:0 2px 6px rgba(0,0,0,.08);z-index:3}
.brand{position:absolute;left:40px;top:26px;display:flex;align-items:center;gap:14px}
.brand-dot{width:56px;height:56px;border-radius:50%;background:var(--rose)}
.brand-name{font-family:'Libre Baskerville',serif;color:var(--rose);font-size:23px;line-height:31px}
.main-nav{position:absolute;top:54px;left:0;width:1200px;font-family:'Libre Baskerville',serif;font-size:14px;color:#222}
.main-nav a{position:absolute;text-decoration:none;color:inherit;white-space:nowrap}
.main-nav a.active{color:var(--red);font-weight:700}

/* hero */
.hero{position:absolute;left:0;top:115px;width:1200px;height:580px;overflow:hidden}
.hero-photo{position:absolute;inset:0;background:linear-gradient(100deg,#eceef1 0%,#e4e6ea 38%,#f0b6a2 55%,#e8502a 72%,#c9361a 100%)}
.hero-title{position:absolute;left:136px;top:138px;font-family:'Libre Baskerville',serif;font-weight:700;color:var(--rose);font-size:54px;line-height:72px}
.hero-text{position:absolute;left:136px;top:287px;width:360px;font-size:15px;line-height:23px;color:#222}
.btn{position:absolute;display:block;background:var(--red);color:var(--white);font-family:'Rubik',sans-serif;font-weight:700;font-size:13px;text-align:center;border-radius:17px;box-shadow:0 2px 4px rgba(0,0,0,.2);text-decoration:none}

/* services */
.service{position:absolute;width:216px;height:216px;border-radius:50%;border:4px solid var(--rose);background:var(--white)}
.service-photo{position:absolute;inset:8px;border-radius:50%;overflow:hidden}
.service-fill{position:absolute;inset:0}
.service-label{position:absolute;left:0;right:0;bottom:0;height:58px;background:var(--rose);color:var(--white);font-family:'Rubik',sans-serif;font-weight:500;font-size:16px;text-align:center;padding-top:12px;letter-spacing:.3px}
.slider-arrow{position:absolute;width:30px;height:30px;border-radius:50%;background:var(--rose);top:935px}

/* remedial */
.remedial{position:absolute;left:0;top:1143px;width:1200px;height:656px;background:var(--mist)}
.remedial-frame{position:absolute;left:94px;top:1308px;width:393px;height:387px;border-top:8px solid var(--rose);border-left:8px solid var(--rose);border-radius:170px 0 0 0}
.remedial-photo{position:absolute;left:104px;top:1318px;width:383px;height:382px;border-radius:160px 0 170px 0;background:linear-gradient(135deg,#c7956e 0%,#e5b48f 40%,#f2d3b6 70%,#d9b07c 100%)}
.remedial-copy{position:absolute;left:541px;top:1280px;width:500px;font-size:16.5px;line-height:30px;color:#333}
.benefits-title{position:absolute;left:544px;top:1520px;color:var(--red);font-size:17px;font-family:'Lato',sans-serif}
.benefit{position:absolute;width:265px;font-family:'Rubik',sans-serif;font-size:16px;line-height:19px;color:#333}
.benefit::before{content:"";position:absolute;left:-24px;top:5px;width:10px;height:10px;border-radius:50%;background:var(--red)}

/* about */
.about-text{position:absolute;left:190px;width:820px;text-align:center;font-size:16.5px;line-height:30px;color:#333}

/* fees */
.fees{position:absolute;left:0;top:2245px;width:1200px;height:506px;background:var(--mist)}
.fee-card{position:absolute;top:2408px;width:140px;height:167px;background:var(--white);border-radius:8px;box-shadow:0 2px 8px rgba(0,0,0,.08);overflow:hidden}
.fee-time{position:absolute;top:2374px;width:76px;height:76px;border-radius:50%;background:var(--rose);color:var(--white);text-align:center;font-family:'Rubik',sans-serif;z-index:2}
.fee-time b{display:block;font-size:25px;font-weight:500;margin-top:12px;line-height:26px}
.fee-time small{display:block;font-size:14px;line-height:16px}
.fee-name{position:absolute;left:0;width:140px;text-align:center;font-family:'Rubik',sans-serif;color:var(--rose);font-size:15px;line-height:27px}
.fee-price{position:absolute;left:0;bottom:0;width:140px;height:38px;background:var(--rose);color:var(--white);font-family:'Rubik',sans-serif;font-weight:700;font-size:25px;text-align:center;line-height:38px}
.fees-note{position:absolute;left:200px;top:2626px;width:800px;text-align:center;font-family:'Rubik',sans-serif;font-size:16px;line-height:30px;color:#222}

/* contact */
.contact-title{position:absolute;left:149px;top:2796px;font-family:'Libre Baskerville',serif;font-weight:700;color:var(--red);font-size:35px}
.field{position:absolute;left:145px;width:385px;border:2px solid var(--rose);border-radius:0 22px 0 22px;background:var(--white);color:var(--salmon);font-family:'Rubik',sans-serif;font-size:13px;padding:14px 0 0 32px}
.map{position:absolute;left:576px;top:2851px;width:501px;height:305px;background:linear-gradient(135deg,#eef0ee 0%,#e6e9e6 55%,#cfe8d8 100%);border:1px solid #ddd}

/* footer */
.site-footer{position:absolute;left:0;top:3270px;width:1200px;height:297px;background:var(--mist)}
.contact-item{position:absolute;top:3392px;font-family:'Rubik',sans-serif;font-size:16px;line-height:26px;color:#222}
.contact-item h4{font-weight:500;font-size:17px;color:#111}
.contact-icon{position:absolute;top:3392px;width:36px;height:36px;border-radius:50%;background:var(--rose)}
.footer-rule{position:absolute;left:107px;top:3508px;width:984px;height:1px;background:var(--rose)}
.copyright{position:absolute;left:0;top:3525px;width:1200px;text-align:center;font-family:'Rubik',sans-serif;font-size:12px;color:#222}
.footer-bar{position:absolute;left:0;top:3554px;width:1200px;height:13px;background:var(--red)}
</style>
</head>
<body>

<header class="site-header">
  <div class="brand">
    <span class="brand-dot"></span>
    <div class="brand-name">STONE BAY<br>MASSAGE</div>
  </div>
  <nav class="main-nav">
    <a class="active" href="#home" style="left:509px">HOME</a>
    <a href="#remedial" style="left:597px">REMEDIAL MASSAGE</a>
    <a href="#about" style="left:787px">ABOUT ME</a>
    <a href="#fees" style="left:900px">FEES</a>
    <a href="#contact" style="left:969px">CONTACT</a>
  </nav>
</header>

<section class="hero" id="home">
  <div class="hero-photo" role="img" aria-label="Red autumn leaves hanging above still water, reflected on the surface"></div>
  <h1 class="hero-title">STONE BAY<br>MASSAGE</h1>
  <p class="hero-text">Remedial massage is used to help relieve tension and stress in the soft tissues of the body</p>
  <a class="btn" href="#contact" style="left:134px;top:355px;width:125px;height:33px;line-height:33px">CONTACT US</a>
  <svg class="abs" style="left:0;top:480px" width="1200" height="100" viewBox="0 0 1200 100">
    <path d="M0 70 C300 30 600 120 1200 40 L1200 100 L0 100 Z" fill="var(--white)"/>
    <path d="M0 68 C260 110 560 95 820 60 C980 38 1100 50 1200 78 L1200 58 C1100 30 980 22 820 40 C560 80 280 88 0 56 Z" fill="var(--rose)"/>
  </svg>
</section>

<h2 class="section-title" style="top:745px">OUR SERVICES</h2>
<span class="slider-arrow" style="left:42px"></span>
<svg class="abs" style="left:42px;top:935px" width="30" height="30" viewBox="0 0 30 30"><path d="M17 9 L11 15 L17 21" stroke="#fff" stroke-width="2.5" fill="none"/></svg>
<span class="slider-arrow" style="left:1123px"></span>
<svg class="abs" style="left:1123px;top:935px" width="30" height="30" viewBox="0 0 30 30"><path d="M13 9 L19 15 L13 21" stroke="#fff" stroke-width="2.5" fill="none"/></svg>

<div class="service" style="left:145px;top:842px">
  <div class="service-photo">
    <div class="service-fill" role="img" aria-label="Hands massaging a client's back" style="background:linear-gradient(160deg,#e9c7b1,#c99276 60%,#8a5a44)"></div>
    <div class="service-label">REMEDIAL</div>
  </div>
</div>
<div class="service" style="left:461px;top:842px">
  <div class="service-photo">
    <div class="service-fill" role="img" aria-label="Pregnant client receiving a gentle massage" style="background:linear-gradient(160deg,#efe6df,#d9b39b 55%,#f5f2ef)"></div>
    <div class="service-label">PREGNANCY</div>
  </div>
</div>
<div class="service" style="left:788px;top:838px;width:228px;height:228px;border-width:5px">
  <div class="service-photo">
    <div class="service-fill" role="img" aria-label="Therapist applying therapeutic treatment to a client's back" style="background:linear-gradient(160deg,#243b5a,#8d5a3d 55%,#c27a55)"></div>
    <div class="service-label" style="height:62px;font-size:18px">THERAPEUTIC</div>
  </div>
</div>

<section class="remedial" id="remedial"></section>
<h2 class="section-title" style="top:1198px">REMEDIAL MASSAGE</h2>
<div class="remedial-frame"></div>
<div class="remedial-photo" role="img" aria-label="Relaxed woman lying face down receiving a shoulder massage, with yellow flowers beside her"></div>
<p class="remedial-copy">Remedial massage is used to help relieve tension and stress in the soft tissues of the body including muscles, tendons, ligaments and connective tissue. It helps to alleviate soft tissue discomfort associated with everyday and occupational stress, over-use injuries e.g. tendinitis, and many chronic pain conditions.&nbsp; An increase in circulation and increased joint flexibility are additional benefits.</p>
<h3 class="benefits-title">Other benefits include:</h3>
<p class="benefit" style="left:574px;top:1558px">Aids in recovery of sporting injuries</p>
<p class="benefit" style="left:574px;top:1614px">Improves joint mobility</p>
<p class="benefit" style="left:574px;top:1652px">Reduces/prevents headaches</p>
<p class="benefit" style="left:574px;top:1689px">Assists with arthritic and rheumatic condition</p>
<p class="benefit" style="left:872px;top:1555px">Assists with pregnancy discomfort</p>
<p class="benefit" style="left:872px;top:1612px">Stimulates local blood supply</p>
<p class="benefit" style="left:872px;top:1649px">Reduces levels of anxiety</p>
<p class="benefit" style="left:872px;top:1687px">Assists in stress management and times of grief</p>

<section id="about">
  <h2 class="section-title" style="top:1862px">ABOUT ME</h2>
  <p class="about-text" style="top:1935px">I completed my training in Toronto, Canada in 1999 where I obtained a Diploma of Remedial Massage through the Northern College of Massage &amp; Bodywork.</p>
  <p class="about-text" style="top:2025px">Over the years, I have practiced in several different settings including medical centre, chiropractic clinic, spa and currently am a sole trader in my own practice. I have been helping my clients achieve better health through my treatments for several years. I take special interest in women's health.</p>
  <a class="btn" href="#about" style="left:537px;top:2157px;width:125px;height:31px;line-height:31px">LEARN MORE</a>
</section>

<section class="fees" id="fees"></section>
<h2 class="section-title" style="top:2287px">FEES</h2>

<div class="fee-card" style="left:175px"><p class="fee-name" style="top:54px">REMEDIAL<br>MASSAGE</p><p class="fee-price">$70</p></div>
<div class="fee-time" style="left:206px"><b>30</b><small>MIN</small></div>
<div class="fee-card" style="left:347px"><p class="fee-name" style="top:54px">REMEDIAL<br>MASSAGE</p><p class="fee-price">$90</p></div>
<div class="fee-time" style="left:378px"><b>45</b><small>MIN</small></div>
<div class="fee-card" style="left:520px"><p class="fee-name" style="top:54px">REMEDIAL<br>MASSAGE</p><p class="fee-price">$110</p></div>
<div class="fee-time" style="left:551px"><b>60</b><small>MIN</small></div>
<div class="fee-card" style="left:696px"><p class="fee-name" style="top:54px">REMEDIAL<br>MASSAGE</p><p class="fee-price">$160</p></div>
<div class="fee-time" style="left:727px"><b>90</b><small>MIN</small></div>
<div class="fee-card" style="left:877px"><p class="fee-name" style="top:26px">MANUAL<br>LYMPHATIC<br>DRAINAGE</p><p class="fee-price">$140</p></div>

<p class="fees-note">I am registered with most health funds. Check your level of cover to see if you are able to claim for remedial massage.</p>

<section id="contact">
  <h2 class="contact-title">CONTACT US</h2>
  <div class="field" style="top:2865px;height:51px">NAME*</div>
  <div class="field" style="top:2938px;height:51px">EMAIL*</div>
  <div class="field" style="top:3014px;height:141px">MESSAGE*</div>
  <a class="btn" href="#contact" style="left:149px;top:3190px;width:89px;height:30px;line-height:30px">SUBMIT</a>
  <div class="map" role="img" aria-label="Street map showing the clinic location"></div>
</section>

<footer class="site-footer">
  <svg class="abs" style="left:0;top:0" width="1200" height="90" viewBox="0 0 1200 90">
    <rect width="1200" height="90" fill="var(--white)"/>
    <path d="M0 45 C300 10 650 10 900 35 C1020 47 1120 40 1200 22 L1200 90 L0 90 Z" fill="var(--mist)"/>
    <path d="M0 48 C300 10 650 10 900 38 C1020 50 1120 42 1200 24 L1200 8 C1110 34 1020 38 900 24 C650 -4 300 -2 0 34 Z" fill="var(--rose)"/>
  </svg>
</footer>

<span class="contact-icon" style="left:141px"></span>
<svg class="abs" style="left:141px;top:3392px" width="36" height="36" viewBox="0 0 36 36"><path d="M18 9c-3.9 0-7 3-7 6.8 0 5 7 11.2 7 11.2s7-6.2 7-11.2C25 12 21.9 9 18 9z" fill="none" stroke="#fff" stroke-width="2"/><circle cx="18" cy="16" r="2.4" fill="none" stroke="#fff" stroke-width="2"/></svg>
<div class="contact-item" style="left:190px"><h4>ADDRESS</h4>Lena Marsh 24 Kestrel Avenue<br>Fernvale VIC 3190</div>

<span class="contact-icon" style="left:509px"></span>
<svg class="abs" style="left:509px;top:3392px" width="36" height="36" viewBox="0 0 36 36"><rect x="10" y="12" width="16" height="12" rx="1.5" fill="none" stroke="#fff" stroke-width="2"/><path d="M10 13 L18 19 L26 13" fill="none" stroke="#fff" stroke-width="2"/></svg>
<div class="contact-item" style="left:552px"><h4>EMAIL</h4>lena@stonebaymassage.com.au</div>

<span class="contact-icon" style="left:900px"></span>
<svg class="abs" style="left:900px;top:3392px" width="36" height="36" viewBox="0 0 36 36"><path d="M13 10c1 0 3 4 3 5s-2 1.5-1.5 3 3 4 4.5 4.5 2-1.5 3-1.5 5 2 5 3-2 3-4 3C17 27 9 19 9 13c0-2 3-3 4-3z" fill="none" stroke="#fff" stroke-width="2" stroke-linejoin="round"/></svg>
<div class="contact-item" style="left:943px"><h4>PHONE</h4>0412 555 019</div>

<div class="footer-rule"></div>
<p class="copyright">COPYRIGHTS 2022@ STONE BAY MASSAGE. ALL RIGHTS RECEIVED</p>
<div class="footer-bar"></div>

</body>
</html>
```